Pagina Lartécnica

The Lartécnica is a company dealing with leasing and selling real estate. The current site can be accessed at www.lartecnica-exemplo.com.br. We intend to redesign the look of the site and for that we would like to redesign the home page and the page with information and pictures of the property. The homepage should maintain the characteristics of the current common design simple, short and straightforward. The page with the data of the properties should be accessed with two changes page as it is currently running. The search from the map by region and should be maintained.
The page containing the information of the property will provide a total of 15 small pictures that when clicked will appear in larger size. The colors to be used should be orange, blue, black and white. The map can be maintained in the current colors.
Updates

Project Deadline Extended
Reason: Payment guarante!!

Payment guaranteed. Deadline for submission of designs April 27.

Industry/Entity Type

Real Estate

Requirements
Must have
• Search by map regions and search box
address
keep colors from the current page
phones
clean look
Nice to have
• clean look
Should not have
• We like the current page. We just want to make it compatible with modern and new design trends and monitors.

```html
<!DOCTYPE html>
<html lang="pt-BR">
<head>
<meta charset="utf-8">
<title>Lartécnica – Detalhes do Imóvel</title>
<link href="https://fonts.googleapis.com/css2?family=PT+Sans:wght@400;700&family=PT+Sans+Narrow:wght@400;700&family=Arimo:wght@400;700&display=swap" rel="stylesheet">
<style>
:root{
  --orange:#f97a10;
  --orange-light:#fb8c22;
  --navy:#2c2f7a;
  --ink:#222;
  --grey-text:#444;
  --panel-grey:#f2f2f2;
  --line:#e4e4e4;
  --footer:#f3f3f3;
  --brown:rgba(90,40,10,.82);
}
*{margin:0;padding:0;box-sizing:border-box}
html,body{width:1200px;height:1113px;overflow:hidden;background:#fff;font-family:"Arimo",Arial,sans-serif;color:var(--ink)}
.page{position:relative;width:1200px;height:1113px}
.band{position:absolute;left:0;top:0;width:1200px;height:172px;background:linear-gradient(180deg,var(--orange-light),var(--orange))}
.nav{position:absolute;top:35px;left:138px;display:flex;gap:31px;font-family:"PT Sans",sans-serif;font-weight:700;font-size:16px;letter-spacing:.7px;color:#fff;text-transform:uppercase}
.phones{position:absolute;left:737px;top:23px;width:339px;height:43px;background:var(--brown);border-radius:2px;color:#fff;font-family:"Arimo",sans-serif;font-size:14px;display:flex;align-items:center;justify-content:center;gap:5px}
.phones b{font-weight:700}
.logo{position:absolute;left:121px;top:89px;width:261px;height:120px;background:#fff;box-shadow:0 6px 10px -4px rgba(0,0,0,.25);display:flex;align-items:center;justify-content:center;gap:10px}
.logo .mark{width:18px;height:18px;background:var(--orange)}
.logo span{font-family:"PT Sans",sans-serif;font-weight:700;font-size:34px;color:var(--navy)}
.side-menu{position:absolute;left:121px;top:226px;width:259px;list-style:none;font-family:"PT Sans",sans-serif;font-weight:700;font-size:15px;color:var(--navy)}
.side-menu li{height:36px;line-height:36px;padding-left:23px;border-bottom:1px solid var(--line)}
.side-menu li:last-child{border-bottom:none}
.search{position:absolute;left:121px;top:385px;width:260px;height:163px;border:1px solid var(--line);border-radius:2px}
.search h3{height:38px;background:var(--orange);color:#fff;font-family:"PT Sans",sans-serif;font-weight:700;font-size:18px;line-height:38px;padding-left:25px}
.radios{position:absolute;top:55px;left:38px;display:flex;font-family:"PT Sans",sans-serif;font-weight:700;font-size:15px;color:var(--grey-text)}
.radio{display:flex;align-items:center;gap:9px}
.radio i{width:16px;height:16px;border-radius:50%;border:1px solid #ccc;background:#f4f4f4;display:inline-block;position:relative}
.radio i.on::after{content:"";position:absolute;left:4px;top:4px;width:6px;height:6px;border-radius:50%;background:#777}
.radio.rent{border-left:1px solid #ddd;margin-left:15px;padding-left:14px}
.select{position:absolute;left:29px;top:91px;width:197px;height:32px;border:1px solid #ddd;font-family:"PT Sans",sans-serif;font-weight:700;font-size:14px;color:var(--grey-text);line-height:30px;padding-left:11px}
.select::after{content:"";position:absolute;right:10px;top:13px;border:5px solid transparent;border-top-color:#888}
.btn-search{position:absolute;left:152px;top:523px;width:196px;height:42px;background:#fff;border:1px solid #ddd;display:flex;align-items:center;justify-content:center;gap:5px;font-family:"PT Sans",sans-serif;font-weight:700;font-size:22px;color:var(--orange)}
.detail{position:absolute;left:416px;top:90px;width:663px;height:872px;background:#fff;border:1px solid var(--line);border-radius:2px}
.detail-head{height:49px;background:var(--panel-grey);display:flex;align-items:center;justify-content:space-between;padding:0 20px 0 22px}
.detail-head h1,.detail h2{font-family:"PT Sans Narrow",sans-serif;font-weight:700;color:var(--navy);font-size:22px}
.photo{position:absolute;left:17px;top:69px;width:320px;height:240px;background:linear-gradient(180deg,#c9d6e4 0%,#e8eef3 35%,#9aa38a 62%,#4d5a2f 100%)}
.map-btn{position:absolute;right:11px;bottom:9px;width:75px;height:35px;background:var(--orange);color:#fff;font-family:"PT Sans",sans-serif;font-weight:700;font-size:13px;display:flex;align-items:center;justify-content:center;gap:6px}
.facts{position:absolute;left:353px;top:68px;font-size:13px;line-height:21px;border-collapse:collapse}
.facts th{color:var(--orange);font-family:"PT Sans",sans-serif;font-weight:700;text-align:left;vertical-align:top;width:74px;font-size:14px}
.like{position:absolute;left:354px;top:280px;display:flex;gap:6px;font-family:"PT Sans",sans-serif;font-size:11px;line-height:14px;color:#333}
.like-btn{width:51px;height:25px;border:1px solid #c8d0e0;background:#eef1f7;border-radius:2px;display:flex;align-items:center;justify-content:center;gap:4px;color:#3b5998;font-size:12px}
.like-btn i,.like .sq{width:11px;height:11px;background:#3b5998;display:inline-block}
.like a{color:#3b5998;text-decoration:none}
.desc{position:absolute;left:19px;top:335px;width:615px}
.desc p{margin-top:5px;font-size:13px;line-height:22px;color:var(--ink)}
.gallery{position:absolute;left:21px;top:457px}
.thumbs{margin-top:10px;display:grid;grid-template-columns:repeat(4,143px);gap:17px 17px;grid-auto-rows:107px}
.thumbs div{width:143px;height:107px}
.footer{position:absolute;left:0;top:998px;width:1200px;height:115px;background:var(--footer);border-top:1px solid #ececec;text-align:center;font-size:13px;color:#555}
.footer .addr{margin-top:31px;font-weight:700}
.footer .addr span{font-weight:400}
.footer .copy{margin-top:24px;font-size:12px;color:#666}
</style>
</head>
<body>
<div class="page">
  <div class="band"></div>
  <nav class="nav"><span>Company</span><span>Location</span><span>Restricted Area</span><span>Contact Us</span></nav>
  <div class="phones"><b>LEASE</b> (48) 3100-2040 &nbsp;|&nbsp; <b>SALES</b> (48) 8100-5522</div>

  <div class="logo"><i class="mark"></i><span>Lartécnica</span></div>

  <ul class="side-menu">
    <li>List your Property</li>
    <li>Information to Owner</li>
    <li>Information for the Tenant</li>
    <li>Request your Property</li>
  </ul>

  <div class="search">
    <h3>Search for Properties</h3>
    <div class="radios">
      <label class="radio">To Buy <i></i></label>
      <label class="radio rent">To Rent <i class="on"></i></label>
    </div>
    <div class="select">All Properties</div>
  </div>
  <div class="btn-search">Buscar
    <svg width="22" height="24" viewBox="0 0 22 24"><circle cx="9" cy="9" r="6.5" fill="none" stroke="#f97a10" stroke-width="3"/><line x1="13.5" y1="14" x2="20" y2="21.5" stroke="#f97a10" stroke-width="3.5" stroke-linecap="round"/></svg>
  </div>

  <main class="detail">
    <div class="detail-head">
      <h1>Detalhes do Imóvel</h1>
      <svg width="24" height="22" viewBox="0 0 24 22"><rect x="5" y="0" width="12" height="9" fill="#2c2f7a"/><rect x="0" y="10" width="24" height="8" rx="1" fill="#2c2f7a"/><rect x="4" y="14" width="16" height="8" fill="#fff" stroke="#2c2f7a" stroke-width="2"/></svg>
    </div>

    <div class="photo" role="img" aria-label="Foto da fachada do prédio residencial cercado de vegetação">
      <div class="map-btn">
        <svg width="14" height="19" viewBox="0 0 14 19"><path d="M7 0C3 0 0 3 0 7c0 5 7 12 7 12s7-7 7-12c0-4-3-7-7-7z" fill="#fff"/><circle cx="7" cy="7" r="2.6" fill="#f97a10"/></svg>Mapa
      </div>
    </div>

    <table class="facts">
      <tr><th>Código:</th><td>A00599</td></tr>
      <tr><th>Bairro:</th><td>Pantano do Sul</td></tr>
      <tr><th>Cidade:</th><td>Florianopolis</td></tr>
      <tr><th>Quartos:</th><td>2</td></tr>
      <tr><th>Endereço:</th><td>Servidão das Palmeiras ,<br>1180 Ap 04 e Ap 05</td></tr>
      <tr><th>Valor:</th><td>900,00</td></tr>
      <tr><th>Cond.:</th><td>0,00</td></tr>
      <tr><th>IPTU:</th><td>16,00</td></tr>
    </table>

    <div class="like">
      <div class="like-btn"><i></i>Like</div>
      <div><span class="sq"></span> 827,226 people like this. <a>Sign Up</a> to<br>see what your friends like.</div>
    </div>

    <section class="desc">
      <h2>Descrição do Imóvel</h2>
      <p>Lorem ipsum dolor sit amet, consectetur adipisicing elit, sed do eiusmod tempor incididunt ut labore et dolore magna aliqua. Ut enim ad minim veniam, quis nostrud exercitation ullamco laboris nisi ut aliquip ex ea commodo consequat.</p>
    </section>

    <section class="gallery">
      <h2>Galeria de Fotos</h2>
      <div class="thumbs">
        <div role="img" aria-label="Fachada do prédio" style="background:linear-gradient(180deg,#6f9bd0,#a9c8c0 50%,#8c8f88)"></div>
        <div role="img" aria-label="Sala com escada e parede vermelha" style="background:linear-gradient(90deg,#e9e6e0 55%,#c73a2e)"></div>
        <div role="img" aria-label="Sala vazia com piso claro" style="background:linear-gradient(180deg,#8c8a84,#d8d4cc)"></div>
        <div role="img" aria-label="Banheiro com azulejos verdes" style="background:linear-gradient(90deg,#7a9a6a,#c9d5c1 50%,#b14a3a)"></div>
        <div role="img" aria-label="Cozinha com janela" style="background:linear-gradient(180deg,#8fb07a,#d7dccf)"></div>
        <div role="img" aria-label="Quarto com janela" style="background:linear-gradient(90deg,#3e4a48,#9fb0ac 50%,#2b2a25)"></div>
        <div role="img" aria-label="Quarto com parede verde" style="background:linear-gradient(90deg,#4e5a26,#a5b05a 60%,#4a3120)"></div>
        <div role="img" aria-label="Banheiro com vaso sanitário" style="background:linear-gradient(90deg,#7d8a86,#c9d0cc 60%,#4a2a1a)"></div>
        <div role="img" aria-label="Vista da varanda" style="background:linear-gradient(180deg,#5d8fd0,#3f5b32 55%,#d8dcda)"></div>
      </div>
    </section>
  </main>

  <footer class="footer">
    <p class="addr">Rua Alameda Verde, 48 - Corner with Marcos Pires Street - Downtown - Florianópolis &nbsp; CEP: <span>88010-400</span> - Fax: (48) <span>3100-2099</span></p>
    <p class="copy">© 2013 - Lartécnica - All Rights Reserved.</p>
  </footer>
</div>
</body>
</html>
```